Simple and clean webdesign for personal homepage

Trying to create a simple and clean webdesign for my personal homepage. Going to use a static site builder with templates to build the site. I want it to have multiple pages - like an about me, blog and resume. I just need something very basic I can customize. I want the main colors to be purple, black and white. I am open to other color palettes too but since purple is my favorite color I want that to be one of the main colors.

The site be mostly text driven. Might have some images in the body text but I want the site design to be light and lean.

Industry/Entity Type

Personal Homepage.

Coding

Coded - Design and coding required

Number of Pages Required

1 page

Font styles to use
Sans Serif

Colors
6B429C
8869AF
B7A5CE
E3DAEB
F3F0F8

Requirements
Must have
• Clean design. Purple used as a color. HTML template.
Nice to have
• Responsive

```html
<!DOCTYPE html>
<html lang="en">
<head>
<meta charset="utf-8">
<title>Daniel Carver — Personal Homepage</title>
<link rel="stylesheet" href="https://fonts.googleapis.com/css2?family=Poppins:wght@400;500;600;700&display=swap">
<style>
:root{
  --purple:#6B429C;
  --purple-mid:#8869AF;
  --purple-soft:#B7A5CE;
  --purple-pale:#E3DAEB;
  --purple-mist:#F3F0F8;
  --ink:#1d1b22;
  --text:#4a4752;
  --white:#ffffff;
  --line:#e6e2ec;
}
*{box-sizing:border-box;margin:0;padding:0}
html,body{width:1200px;height:4440px;overflow:hidden}
body{font-family:"Poppins",sans-serif;color:var(--ink);background:var(--white);position:relative}
p{font-size:14px;line-height:24px;color:var(--text)}

.section-title{font-size:32px;font-weight:600;text-align:center;position:relative;display:inline-block;padding-bottom:10px}
.section-title::after{content:"";position:absolute;left:50%;bottom:0;width:120px;height:3px;margin-left:-60px;background:var(--ink)}
.title-wrap{text-align:center}
.section-intro{width:760px;margin:26px auto 0;text-align:center;font-size:14px;line-height:30px}

/* hero */
.hero{position:relative;height:600px;background:linear-gradient(180deg,#f6f5f8 0%,#eeedf2 100%);overflow:hidden}
.hero-art{position:absolute;inset:0;background:radial-gradient(circle at 70% 40%,rgba(183,165,206,.18),transparent 55%),radial-gradient(circle at 20% 70%,rgba(183,165,206,.12),transparent 50%)}
.site-nav{position:absolute;top:26px;left:100px;right:100px;display:flex;justify-content:space-between;align-items:center}
.brand{font-size:28px;font-weight:500;color:var(--ink)}
.nav-links{display:flex;gap:44px;list-style:none;font-size:16px;font-weight:500}
.nav-links li{padding-bottom:4px}
.nav-links .active{color:var(--purple);border-bottom:2px solid var(--purple)}
.hero-copy{position:absolute;top:190px;left:0;right:0;text-align:center}
.hero-hello{font-size:24px;color:var(--purple);font-weight:500}
.hero-headline{font-size:38px;font-weight:700;line-height:52px;margin-top:16px}
.btn{display:inline-block;background:var(--purple);color:var(--white);font-size:16px;font-weight:500;padding:12px 32px;border-radius:3px}
.hero .btn{margin-top:30px}

/* about */
.about{height:320px;background:var(--purple);display:flex;align-items:center;padding:0 100px;gap:40px}
.about-title{width:260px;color:var(--white);font-size:36px;font-weight:500;text-align:center;position:relative;padding-bottom:8px;align-self:center;margin-top:-20px}
.about-title::after{content:"";position:absolute;left:0;right:0;bottom:-4px;height:2px;background:var(--white)}
.about-cols{display:flex;gap:40px;flex:1}
.about-cols p{color:var(--white);font-size:14px;line-height:22px;flex:1}

/* works */
.works{height:630px;padding-top:96px}
.work-grid{display:flex;gap:40px;padding:0 100px;margin-top:44px}
.work-card{flex:1;min-height:312px;border:1px solid var(--line);box-shadow:0 4px 18px rgba(60,40,90,.08);padding:26px 22px 22px}
.work-card svg{width:56px;height:56px;display:block}
.work-card h3{font-size:21px;font-weight:600;margin:14px 0 8px;line-height:30px}
.work-card p{font-size:12.5px;line-height:20px}

/* skills */
.skills{height:620px;background:var(--purple-mist);padding-top:80px}
.skill-grid{display:grid;grid-template-columns:420px 420px;column-gap:80px;row-gap:34px;justify-content:center;margin-top:40px}
.skill-head{display:flex;justify-content:space-between;font-size:14px;margin-bottom:8px}
.skill-track{height:16px;background:var(--purple-soft);border-radius:8px;overflow:hidden}
.skill-fill{height:100%;background:var(--purple);border-radius:8px}

/* experience */
.experience{height:1010px;padding-top:80px;position:relative}
.timeline{position:relative;margin-top:50px;height:720px}
.timeline::before{content:"";position:absolute;left:595px;top:0;bottom:20px;border-left:2px dashed #c9c4d2}
.tl-item{position:absolute;left:0;right:0;height:140px}
.tl-item h3{position:absolute;left:100px;top:20px;width:330px;font-size:19px;font-weight:600;line-height:30px}
.tl-dot{position:absolute;left:585px;top:0;width:22px;height:22px;border:2px solid #a9a3b4;background:var(--white);border-radius:50%}
.tl-date{position:absolute;left:440px;width:124px;text-align:right;top:28px;font-size:12px;color:var(--text);white-space:nowrap}
.tl-item p{position:absolute;left:716px;top:20px;width:390px;font-size:13px;line-height:22px}

/* blog */
.blog{height:480px;background:var(--purple-mist);padding-top:70px}
.blog-grid{display:flex;gap:40px;padding:0 100px;margin-top:40px}
.blog-card{flex:1;height:236px;background:var(--white);box-shadow:0 4px 16px rgba(60,40,90,.08);padding:24px}
.blog-date{font-size:12px;color:var(--text);display:flex;align-items:center;gap:8px}
.blog-date i{width:14px;height:14px;background:var(--purple);display:inline-block;border-radius:2px}
.blog-card h3{font-size:17px;font-weight:700;line-height:24px;margin:12px 0 10px}
.blog-card p{font-size:13px;line-height:20px}
.read-more{font-size:13px;color:var(--purple);font-weight:600;margin-top:10px;display:block}

/* contact */
.contact{height:380px;display:flex}
.contact-form-area{position:relative;width:655px;padding:44px 110px}
.contact-photo{position:absolute;inset:0;background:linear-gradient(135deg,#e9e9ec 0%,#d9d9de 60%,#cfcfd6 100%)}
.contact-form-area > *:not(.contact-photo){position:relative}
.contact-form-area h2{font-size:36px;font-weight:600;margin-bottom:18px}
.form-row{display:flex;gap:4px;margin-bottom:4px}
.field{flex:1;height:52px;background:var(--white);border:1px solid #d8d6dd;font-size:12px;padding:8px 12px;color:var(--text)}
.field.message{height:76px}
.contact .btn{margin-top:18px;font-size:13px;padding:10px 36px}
.contact-info{flex:1;background:var(--purple);color:var(--white);padding:38px 120px 0 120px}
.contact-info h2{font-size:36px;font-weight:500;display:inline-block;border-bottom:2px solid var(--white);padding-bottom:2px}
.visit{font-size:13px;font-weight:600;margin:18px 0 14px}
.info-row{display:flex;align-items:center;gap:18px;margin-bottom:18px;font-size:13px;line-height:19px}
.info-row .icon{width:34px;height:34px;border-radius:50%;background:var(--white);display:flex;align-items:center;justify-content:center;flex:none}
.info-row strong{font-size:18px;font-weight:600}

/* footer */
.site-footer{height:440px;background:var(--purple-mid);text-align:center;color:var(--white);padding-top:90px}
.footer-brand{font-size:56px;font-weight:500}
.footer-links{display:flex;justify-content:center;gap:40px;list-style:none;font-size:16px;margin-top:18px}
.copyright{font-size:13px;margin-top:22px;color:var(--white)}
.social{display:flex;justify-content:center;gap:14px;margin-top:30px}
.social span{width:38px;height:38px;border-radius:50%;background:var(--white)}
</style>
</head>
<body>

<header class="hero">
  <div class="hero-art" role="img" aria-label="Soft abstract line artwork in pale grey behind the introduction"></div>
  <nav class="site-nav">
    <div class="brand">Logo</div>
    <ul class="nav-links">
      <li class="active">Home</li><li>About Me</li><li>Blog</li><li>Resume</li><li>My Work</li><li>Contact</li>
    </ul>
  </nav>
  <div class="hero-copy">
    <div class="hero-hello">Hi, I'm Daniel Carver</div>
    <h1 class="hero-headline">An independent software contractor,<br>architect &amp; tech trainer</h1>
    <span class="btn">View Resume</span>
  </div>
</header>

<section class="about">
  <h2 class="about-title">About Me</h2>
  <div class="about-cols">
    <p>Lorem ipsum dolor sit amet, consectetur adipiscing elit, sed do eiusmod tempor incididunt ut labore et dolore magna aliqua. Quis ipsum suspendisse ultrices gravida. Risus commodo viverra maecenas accumsan lacus vel facilisis.</p>
    <p>Lorem ipsum dolor sit amet, consectetur adipiscing elit, sed do eiusmod tempor incididunt ut labore et dolore magna aliqua. Quis ipsum suspendisse ultrices gravida. Risus commodo viverra maecenas accumsan lacus vel facilisis.</p>
  </div>
</section>

<section class="works">
  <div class="title-wrap"><h2 class="section-title">Our Works</h2></div>
  <p class="section-intro">Lorem ipsum dolor sit amet, consectetur adipiscing elit, sed do eiusmod tempor incididunt ut labore et dolore magna aliqua. Quis ipsum suspendisse ultrices gravida.</p>
  <div class="work-grid">
    <article class="work-card">
      <svg viewBox="0 0 64 64" fill="none" stroke="#6B429C" stroke-width="3" stroke-linecap="round"><path d="M10 54 L38 26"/><path d="M36 18 a10 10 0 1 0 10 10 l-6-2 -2-6z"/><path d="M14 12 l8 8 -4 4 -8-8z"/><path d="M22 22 L52 52"/></svg>
      <h3>Finibus Bonorum et</h3>
      <p>Lorem ipsum dolor sit amet, consectetur adipiscing elit, sed do eiusmod tempor incididunt ut labore et dolore magna aliqua. Quis ipsum suspendisse ultrices gravida. Risus commodo viverra maecenas accumsan lacus vel facilisis.</p>
    </article>
    <article class="work-card">
      <svg viewBox="0 0 64 64" fill="none" stroke="#6B429C" stroke-width="3"><circle cx="32" cy="32" r="10"/><circle cx="32" cy="32" r="22" stroke-dasharray="8 6"/></svg>
      <h3>Finibus Bonorum et</h3>
      <p>Lorem ipsum dolor sit amet, consectetur adipiscing elit, sed do eiusmod tempor incididunt ut labore et dolore magna aliqua. Quis ipsum suspendisse ultrices gravida. Risus commodo viverra maecenas accumsan lacus vel facilisis.</p>
    </article>
    <article class="work-card">
      <svg viewBox="0 0 64 64" fill="none" stroke="#6B429C" stroke-width="3" stroke-linecap="round" stroke-linejoin="round"><path d="M6 46 h12 l10 4 h14 l14-10"/><path d="M18 46 v-8 h10 l8 4"/><circle cx="36" cy="20" r="10"/></svg>
      <h3>Finibus Bonorum et</h3>
      <p>Lorem ipsum dolor sit amet, consectetur adipiscing elit, sed do eiusmod tempor incididunt ut labore et dolore magna aliqua. Quis ipsum suspendisse ultrices gravida. Risus commodo viverra maecenas accumsan lacus vel facilisis.</p>
    </article>
  </div>
</section>

<section class="skills">
  <div class="title-wrap"><h2 class="section-title">Skills</h2></div>
  <p class="section-intro">Lorem ipsum dolor sit amet, consectetur adipiscing elit, sed do eiusmod tempor incididunt ut labore et dolore magna aliqua. Quis ipsum suspendisse ultrices gravida.</p>
  <div class="skill-grid">
    <div><div class="skill-head"><span>Skill 1</span><span>80%</span></div><div class="skill-track"><div class="skill-fill" style="width:80%"></div></div></div>
    <div><div class="skill-head"><span>Skill 5</span><span>80%</span></div><div class="skill-track"><div class="skill-fill" style="width:80%"></div></div></div>
    <div><div class="skill-head"><span>Skill 2</span><span>75%</span></div><div class="skill-track"><div class="skill-fill" style="width:75%"></div></div></div>
    <div><div class="skill-head"><span>Skill 6</span><span>85%</span></div><div class="skill-track"><div class="skill-fill" style="width:85%"></div></div></div>
    <div><div class="skill-head"><span>Skill 3</span><span>75%</span></div><div class="skill-track"><div class="skill-fill" style="width:75%"></div></div></div>
    <div><div class="skill-head"><span>Skill 7</span><span>80%</span></div><div class="skill-track"><div class="skill-fill" style="width:80%"></div></div></div>
    <div><div class="skill-head"><span>Skill 4</span><span>90%</span></div><div class="skill-track"><div class="skill-fill" style="width:90%"></div></div></div>
    <div><div class="skill-head"><span>Skill 8</span><span>80%</span></div><div class="skill-track"><div class="skill-fill" style="width:80%"></div></div></div>
  </div>
</section>

<section class="experience">
  <div class="title-wrap"><h2 class="section-title">Experience</h2></div>
  <p class="section-intro">Lorem ipsum dolor sit amet, consectetur adipiscing elit, sed do eiusmod tempor incididunt ut labore et dolore magna aliqua. Quis ipsum suspendisse ultrices gravida.</p>
  <div class="timeline">
    <div class="tl-item" style="top:0">
      <span class="tl-dot"></span>
      <h3>The standard Lorem Ipsum passage, used since the 1500s</h3>
      <span class="tl-date">June 2018 – Present</span>
      <p>Lorem ipsum dolor sit amet, consectetur adipiscing elit, sed do eiusmod tempor incididunt ut labore et dolore magna aliqua. Quis ipsum suspendisse ultrices gravida. Risus commodo viverra maecenas.</p>
    </div>
    <div class="tl-item" style="top:180px">
      <span class="tl-dot"></span>
      <h3>The standard Lorem Ipsum passage, used since the 1500s</h3>
      <span class="tl-date">June 2018 – Present</span>
      <p>Lorem ipsum dolor sit amet, consectetur adipiscing elit, sed do eiusmod tempor incididunt ut labore et dolore magna aliqua. Quis ipsum suspendisse ultrices gravida. Risus commodo viverra maecenas.</p>
    </div>
    <div class="tl-item" style="top:360px">
      <span class="tl-dot"></span>
      <h3>The standard Lorem Ipsum passage, used since the 1500s</h3>
      <span class="tl-date">June 2018 – Present</span>
      <p>Lorem ipsum dolor sit amet, consectetur adipiscing elit, sed do eiusmod tempor incididunt ut labore et dolore magna aliqua. Quis ipsum suspendisse ultrices gravida. Risus commodo viverra maecenas.</p>
    </div>
    <div class="tl-item" style="top:540px">
      <span class="tl-dot"></span>
      <h3>The standard Lorem Ipsum passage, used since the 1500s</h3>
      <span class="tl-date">June 2018 – Present</span>
      <p>Lorem ipsum dolor sit amet, consectetur adipiscing elit, sed do eiusmod tempor incididunt ut labore et dolore magna aliqua. Quis ipsum suspendisse ultrices gravida. Risus commodo viverra maecenas.</p>
    </div>
  </div>
</section>

<section class="blog">
  <div class="title-wrap"><h2 class="section-title">Latest Blog</h2></div>
  <div class="blog-grid">
    <article class="blog-card">
      <div class="blog-date"><i></i>Jun 20,2022</div>
      <h3>The standard Lorem Ipsum passage, used since</h3>
      <p>Lorem ipsum dolor sit amet, consectetur adipiscing elit, sed do eiusmod tempor incididunt ut labore et dolore magna aliqua.</p>
      <span class="read-more">Learn More &gt;</span>
    </article>
    <article class="blog-card">
      <div class="blog-date"><i></i>Jun 20,2022</div>
      <h3>The standard Lorem Ipsum passage, used since</h3>
      <p>Lorem ipsum dolor sit amet, consectetur adipiscing elit, sed do eiusmod tempor incididunt ut labore et dolore magna aliqua.</p>
      <span class="read-more">Learn More &gt;</span>
    </article>
    <article class="blog-card">
      <div class="blog-date"><i></i>Jun 20,2022</div>
      <h3>The standard Lorem Ipsum passage, used since</h3>
      <p>Lorem ipsum dolor sit amet, consectetur adipiscing elit, sed do eiusmod tempor incididunt ut labore et dolore magna aliqua.</p>
      <span class="read-more">Learn More &gt;</span>
    </article>
  </div>
</section>

<section class="contact">
  <div class="contact-form-area">
    <div class="contact-photo" role="img" aria-label="Muted photo of a desk workspace with a laptop behind the contact form"></div>
    <h2>Get In Touch</h2>
    <div class="form-row"><div class="field">Name</div><div class="field">Phone</div></div>
    <div class="form-row"><div class="field">Email address</div><div class="field">Subject</div></div>
    <div class="form-row"><div class="field message">Message</div></div>
    <span class="btn">SUBMIT</span>
  </div>
  <div class="contact-info">
    <h2>Contact Us</h2>
    <div class="visit">OUR VISIT US</div>
    <div class="info-row">
      <span class="icon"><svg width="16" height="16" viewBox="0 0 24 24" fill="#6B429C"><path d="M12 2a7 7 0 0 0-7 7c0 5 7 13 7 13s7-8 7-13a7 7 0 0 0-7-7zm0 9.5A2.5 2.5 0 1 1 12 6.5a2.5 2.5 0 0 1 0 5z"/></svg></span>
      <span>48 Orchard Lane,<br>Fairview 90210</span>
    </div>
    <div class="info-row">
      <span class="icon"><svg width="16" height="16" viewBox="0 0 24 24" fill="#6B429C"><path d="M6.6 10.8a15 15 0 0 0 6.6 6.6l2.2-2.2a1 1 0 0 1 1-.25 11.4 11.4 0 0 0 3.6.6 1 1 0 0 1 1 1V20a1 1 0 0 1-1 1A17 17 0 0 1 3 4a1 1 0 0 1 1-1h3.5a1 1 0 0 1 1 1 11.4 11.4 0 0 0 .6 3.6 1 1 0 0 1-.25 1z"/></svg></span>
      <span>Call Us Today!<br><strong>555 - 014 - 2277</strong></span>
    </div>
    <div class="info-row">
      <span class="icon"><svg width="16" height="16" viewBox="0 0 24 24" fill="#6B429C"><path d="M3 5h18v14H3z M3 5l9 7 9-7" stroke="#fff" stroke-width="1.5"/></svg></span>
      <span>Email Us<br><strong>hello@carvermail.net</strong></span>
    </div>
  </div>
</section>

<footer class="site-footer">
  <div class="footer-brand">Logo</div>
  <ul class="footer-links"><li>Home</li><li>About Me</li><li>Blog</li><li>Resume</li><li>My Work</li><li>Contact</li></ul>
  <p class="copyright">© Copyright 2022 Carver Studio. All rights reserved.</p>
  <div class="social"><span></span><span></span><span></span><span></span></div>
</footer>

</body>
</html>
```